Website To Serve As A Resource For Medical Conditions

I need a website that is attractive that will be utilized to educate patients on either hepatitis c or HIV so it should be easily readable attractive but also professional. This website is going to be furnished with various topics for example, HIV treatment, THRIVE AND NOURISH, HIV and Exercise, HIV and....

This website will also be cloned and utilized similarly for Hepatitis.

Coded - Design and coding required

1 page

0094D4
00A9DD
6FCCEA
C7EBF8
E9F6FB
A7469A
B969AE
D3A5CF
EDDBEB
F8F0F9
6B429C
8869AF
B7A5CE
E3DAEB
F3F0F8

```html
<!DOCTYPE html>
<html lang="en">
<head>
<meta charset="utf-8">
<title>Thrive and Nourish</title>
<link href="https://fonts.googleapis.com/css2?family=Fira+Sans+Condensed:wght@600;700;800&family=PT+Sans:wght@400;700&display=swap" rel="stylesheet">
<style>
:root{
  --orange:#f5a11c;
  --ink:#111111;
  --dark:#231f20;
  --grey:#58585a;
  --white:#ffffff;
  --hero-a:#c9cfd3;
  --hero-b:#f4f6f7;
  --news-a:#3a0608;
  --news-b:#120304;
  --peach:#fde4c8;
  --navy:#1d4a88;
  --blush:#f6ece8;
}
*{margin:0;padding:0;box-sizing:border-box}
html,body{width:1200px;height:3132px;overflow:hidden}
body{position:relative;background:var(--white);font-family:"PT Sans",sans-serif;color:var(--ink)}
.abs{position:absolute}
.heading{font-family:"Fira Sans Condensed",sans-serif;font-weight:700;text-transform:uppercase}

/* header */
.topbar{left:0;top:0;width:1200px;height:8px;background:var(--orange)}
.site-header{left:0;top:8px;width:1200px;height:78px;background:var(--white)}
.brand{left:170px;top:22px;display:flex;align-items:center;gap:10px}
.brand-dot{width:26px;height:26px;border-radius:50%;background:var(--orange)}
.brand-name{font-family:"PT Sans",sans-serif;font-weight:700;font-size:21px;line-height:23px;color:var(--dark)}
.nav{left:550px;top:28px;display:flex;gap:17px;font-size:15px;font-weight:700;color:var(--dark);letter-spacing:.2px}
.donate{left:929px;top:29px;width:99px;height:36px;border-radius:18px;background:var(--orange);font-weight:700;font-size:17px;display:flex;align-items:center;justify-content:center}

/* hero */
.hero{left:0;top:86px;width:1200px;height:647px;background:radial-gradient(ellipse at 52% 45%,var(--hero-b) 0%,#e6e9eb 40%,var(--hero-a) 100%)}
.hero-title{left:172px;top:200px;font-family:"Fira Sans Condensed",sans-serif;font-weight:800;font-size:64px;line-height:68px;letter-spacing:-.5px}
.hero-text{left:173px;top:352px;width:598px;font-size:17.5px;line-height:24.5px;font-weight:700;text-align:justify}
.btn-dark{left:173px;top:460px;width:159px;height:58px;border-radius:29px;background:var(--ink);color:var(--white);font-size:20px;font-weight:700;display:flex;align-items:center;justify-content:center}
.hero-visual{left:815px;top:118px;width:190px;height:582px;border-radius:95px 95px 30px 30px;background:linear-gradient(180deg,#dfe3e6 0%,#c2262b 30%,#8f1418 55%,#cfd3d6 85%,#b9bec2 100%)}

/* support */
.support-title{left:0;top:796px;width:1200px;text-align:center;font-size:40px;letter-spacing:.2px}
.topic{width:333px;height:333px;top:885px;border-radius:50%;overflow:hidden}
.topic-art{position:absolute;left:0;top:0;width:333px;height:240px}
.topic-band{position:absolute;left:-30px;top:225px;width:393px;height:240px;border-radius:50%;display:flex;justify-content:center;padding-top:22px;color:var(--white);font-family:"Fira Sans Condensed",sans-serif;font-weight:700;font-size:31px}
.topic-1{left:67px;background:var(--peach)}
.topic-2{left:434px;background:var(--navy)}
.topic-3{left:793px;background:var(--blush)}
.band-grey{background:var(--grey)}
.band-orange{background:var(--orange)}
.support-text{left:180px;top:1262px;width:840px;text-align:center;font-size:13.5px;line-height:22.5px}

/* news */
.news{left:0;top:1440px;width:1200px;height:687px;background:radial-gradient(circle at 30% 25%,#5a0d10 0%,transparent 35%),radial-gradient(circle at 80% 70%,#4a0a0c 0%,transparent 40%),linear-gradient(180deg,var(--news-a),var(--news-b))}
.news-title{left:0;top:1497px;width:1200px;text-align:center;color:var(--white);font-size:40px}
.news-sub{left:170px;top:1559px;width:860px;text-align:center;color:var(--white);font-size:15.5px;line-height:22.5px}
.card{top:1661px;width:277px;height:375px;background:var(--white)}
.card-1{left:173px}.card-2{left:462px}.card-3{left:750px}
.card-photo{position:absolute;left:10px;top:10px;width:257px;height:190px}
.card-title{position:absolute;left:0;top:214px;width:277px;text-align:center;font-size:24px}
.card-text{position:absolute;left:12px;top:250px;width:253px;text-align:center;font-size:13px;line-height:19.5px}
.card-btn{position:absolute;left:86px;top:318px;width:106px;height:40px;border-radius:20px;color:var(--white);font-weight:700;font-size:15.5px;display:flex;align-items:center;justify-content:center}

/* guidelines */
.guide-art{left:180px;top:2189px;width:380px;height:389px;border-radius:40px;background:radial-gradient(circle at 50% 45%,#e23b2a 0%,#d2382b 28%,#f7d3b4 30%,#fbe3cc 70%,#ffffff 100%)}
.guide-title{left:609px;top:2205px;width:460px;font-size:40px;line-height:40px;white-space:nowrap}
.guide-list{left:609px;top:2352px;list-style:none;font-size:18.5px;font-weight:700;line-height:33.8px}
.guide-list li{display:flex;align-items:center;gap:12px}
.bullet{width:12px;height:12px;border-radius:50%;background:var(--orange)}

/* footer */
.footer{left:0;top:2639px;width:1200px;height:493px;background:var(--dark)}
.foot-brand{left:172px;top:2780px;width:170px;display:flex;flex-direction:column;align-items:center;gap:12px}
.foot-dot{width:42px;height:42px;border-radius:50%;background:var(--orange)}
.foot-name{color:var(--white);font-weight:700;font-size:30px;line-height:34px;text-align:center}
.foot-head{color:var(--white);font-size:26px;font-family:"Fira Sans Condensed",sans-serif;font-weight:600;text-transform:uppercase;letter-spacing:.5px}
.links{color:var(--white);font-size:15.5px;line-height:31px;list-style:none}
.contact{left:733px;display:flex;align-items:flex-start;gap:12px;color:var(--white);font-size:21px;font-weight:700}
.icon{width:40px;height:40px;border-radius:50%;background:var(--orange);display:flex;align-items:center;justify-content:center;flex:none}
.divider{left:173px;top:3060px;width:855px;height:1px;background:#8a8788}
.copyright{left:0;top:3085px;width:1200px;text-align:center;color:var(--white);font-family:"Fira Sans Condensed",sans-serif;font-weight:600;font-size:16px}
</style>
</head>
<body>

<div class="abs topbar"></div>
<header class="abs site-header"></header>
<div class="abs brand"><span class="brand-dot"></span><span class="brand-name">THRIVE AND<br>NOURISH</span></div>
<nav class="abs nav"><span>HOME</span><span>ABOUT US</span><span>WHAT WE DO</span><span>GET INVOLVED</span></nav>
<div class="abs donate">DONATE</div>

<section class="abs hero"></section>
<h1 class="abs hero-title">END THE DREAD<br>STOP THE SPREAD</h1>
<p class="abs hero-text">Duis aute irure dolor in reprehenderit in voluptate velit esse cillum dolore eu fugiat nulla pariatur. Excepteur sint occaecat cupidatat non proident, sunt in culpa qui officia deserunt mollit anim id est laborum</p>
<div class="abs btn-dark">READ MORE</div>
<div class="abs hero-visual" role="img" aria-label="Syringe wrapped in a red awareness ribbon"></div>

<h2 class="abs heading support-title">Your Support Can Change Lives</h2>
<div class="abs topic topic-1">
  <div class="topic-art" role="img" aria-label="Illustration of people exercising with weights"></div>
  <div class="topic-band band-grey">HIV &amp; EXERCISE</div>
</div>
<div class="abs topic topic-2">
  <div class="topic-art" role="img" aria-label="Illustration of a patient coughing beside a lung diagram"></div>
  <div class="topic-band band-orange">HIV TREATMENT</div>
</div>
<div class="abs topic topic-3">
  <div class="topic-art" role="img" aria-label="Illustration of a person surrounded by health symbols"></div>
  <div class="topic-band band-grey">HIV &amp; NUTRITION</div>
</div>
<p class="abs support-text">Nemo enim ipsam voluptatem quia voluptas sit aspernatur aut odit aut fugit, sed quia consequuntur magni dolores eos qui ratione voluptatem sequi nesciunt. Neque porro quisquam est, qui dolorem ipsum quia dolor sit amet, consectetur, adipisci velit, sed quia non numquam eius modi tempora incidunt ut labore et dolore magnam aliquam quaerat voluptatem. Ut enim ad minima veniam, quis nostrum exercitationem ullam corporis suscipit laboriosam, nisi ut aliquid ex ea commodi consequatur? Quis autem vel eum iure reprehenderit qui in ea voluptate velit esse quam nihil molestiae consequatur, vel illum qui dolorem eum fugiat quo voluptas nulla pariatur</p>

<section class="abs news" role="img" aria-label="Dark red background of magnified virus particles"></section>
<h2 class="abs heading news-title">Latest News</h2>
<p class="abs news-sub">Nemo enim ipsam voluptatem quia voluptas sit aspernatur aut odit aut fugit, sed quia consequuntur magni dolores eos qui ratione voluptatem sequi nesciunt.</p>

<article class="abs card card-1">
  <div class="card-photo" role="img" aria-label="Photo of a gloved hand giving an injection in the shoulder" style="background:linear-gradient(135deg,#c9d2e4,#e8d7c9 60%,#f2efec)"></div>
  <h3 class="heading card-title">Duis Aute Irure</h3>
  <p class="card-text">Quis autem vel eum iure reprehenderit qui in ea voluptate velit esse quam nihil molestiae consequatur.</p>
  <div class="card-btn" style="background:var(--grey)">Read More</div>
</article>
<article class="abs card card-2">
  <div class="card-photo" role="img" aria-label="Photo of a lab worker handling blood sample tubes" style="background:linear-gradient(135deg,#dfe5ec,#8fb4de 50%,#e7ecef)"></div>
  <h3 class="heading card-title">Duis Aute Irure</h3>
  <p class="card-text">Quis autem vel eum iure reprehenderit qui in ea voluptate velit esse quam nihil molestiae consequatur.</p>
  <div class="card-btn" style="background:var(--orange)">Read More</div>
</article>
<article class="abs card card-3">
  <div class="card-photo" role="img" aria-label="Photo of a doctor consulting with a seated patient" style="background:linear-gradient(135deg,#f0a070,#e9e3df 45%,#7f8fa6)"></div>
  <h3 class="heading card-title">Duis Aute Irure</h3>
  <p class="card-text">Quis autem vel eum iure reprehenderit qui in ea voluptate velit esse quam nihil molestiae consequatur.</p>
  <div class="card-btn" style="background:var(--grey)">Read More</div>
</article>

<div class="abs guide-art" role="img" aria-label="Illustration of open hands holding a red awareness ribbon"></div>
<h2 class="abs heading guide-title">Health Protection<br>Office (HPO) Guideline<br>Reports</h2>
<ul class="abs guide-list">
  <li><span class="bullet"></span>Pre-exposure Prophylaxis (PrEP)</li>
  <li><span class="bullet"></span>Occupational Postexposure Prophylaxis (PEP)</li>
  <li><span class="bullet"></span>Nonoccupational Postexposure Prophylaxis</li>
  <li><span class="bullet"></span>Prevention with Persons with HIV</li>
  <li><span class="bullet"></span>Types of Testing</li>
  <li><span class="bullet"></span>Hormonal Contraception</li>
</ul>

<footer class="abs footer"></footer>
<div class="abs foot-brand"><span class="foot-dot"></span><span class="foot-name">THRIVE AND<br>NOURISH</span></div>
<h3 class="abs foot-head" style="left:416px;top:2713px">Useful Links</h3>
<ul class="abs links" style="left:417px;top:2760px"><li>FAQs</li><li>Careers</li><li>Contact Us</li><li>Disclaimer</li><li>Success Stories</li><li>Payback Policy</li></ul>
<ul class="abs links" style="left:560px;top:2760px"><li>Privacy Policy</li><li>Terms Of Conditions</li><li>Donor Login</li><li>News &amp; Blogs</li></ul>
<h3 class="abs foot-head" style="left:733px;top:2713px">Contact Us</h3>

<div class="abs contact" style="top:2760px">
  <span class="icon"><svg width="20" height="20" viewBox="0 0 24 24" fill="none" stroke="#231f20" stroke-width="2"><path d="M5 3h4l2 5-2.5 1.5a11 11 0 0 0 6 6L16 13l5 2v4a2 2 0 0 1-2 2A16 16 0 0 1 3 5a2 2 0 0 1 2-2z"/></svg></span>
  <span style="padding-top:6px">+00-12-3456-7890</span>
</div>
<div class="abs contact" style="top:2812px">
  <span class="icon"><svg width="20" height="20" viewBox="0 0 24 24" fill="none" stroke="#231f20" stroke-width="2"><rect x="3" y="5" width="18" height="14" rx="1"/><path d="M3 6l9 7 9-7"/></svg></span>
  <span style="padding-top:6px">hello@thrivenourish.example</span>
</div>
<div class="abs contact" style="top:2865px">
  <span class="icon"><svg width="20" height="20" viewBox="0 0 24 24" fill="none" stroke="#231f20" stroke-width="2"><circle cx="12" cy="12" r="9"/><path d="M3 12h18M12 3c3 3 3 15 0 18M12 3c-3 3-3 15 0 18"/></svg></span>
  <span style="padding-top:6px">www.thrivenourish.example</span>
</div>
<div class="abs contact" style="top:2917px">
  <span class="icon"><svg width="20" height="20" viewBox="0 0 24 24" fill="none" stroke="#231f20" stroke-width="2"><path d="M12 22s7-7 7-12a7 7 0 0 0-14 0c0 5 7 12 7 12z"/><circle cx="12" cy="10" r="2.5"/></svg></span>
  <span style="padding-top:6px;line-height:29px">14 Maple Row<br>Riverside Quarter,<br>ZX 4020</span>
</div>

<div class="abs divider"></div>
<p class="abs copyright">Copyrights @ 2023 Al Rights Reserved.</p>

</body>
</html>
```